Calverdane Group
Branding Material: 1 Tri-fold corporate brochure, 4 single-sided brochures, 1 Presentation Folder
Our company requires the following branding material:
1) One tri-fold, double sided, full color corporate brochure (8.5" X 11" Size)
2) Four, single sided, full color company profile brochures. (One company profile brochure for each company under the Calverdane Group - for a total of 4. 8.5" X 11" Size)
3) Presentation Folder (To place the 4 company profile brochures in. 9" X 12" Size)
Our target audience: Industrial buyers, wholesalers, manufacturerers, suppliers of lumber and panel products, large industries.
We have recently redesigned our logos, business cards, and letterheads. The branding material which we request must creatively and artistically correspond to our new business cards, logos, and letterheads. We are creating a brand in which elements such as message, font, typeface, theme, colors, and “feel” are consistent across all marketing platforms.
Corporate Logo (CALVERDANE GROUP)
Logo for our flagship company under the Calverdane Group.
Logo for our trading company in Dubai.
Logo for our manufacturing subsidiary.
Logo for our logistics subsidiary.
The content for the tri-fold, double sided, full color corporate brochure.
Font and color information regarding our logos.
The content for the FIRST company profile brochure (single page)
The content for the SECOND company profile brochure (single page)
The content for the THIRD company profile brochure (single page)
The content for the FOURTH company profile (single page)
AI file format for CALVERDANE GROUP logo
AI File format for CALVERDANE TIMBER GOODS logo
AI file format for CALVERDANE TRANSLINK INC logo
AI file format for CALVERDANE TIMBER GOODS DUBAI logo
AI file format for CALVERDANE BOARD MILLS LLC logo

```html
<!DOCTYPE html>
<html lang="en">
<head>
<meta charset="utf-8">
<title>Calverdane Group – Presentation Folder</title>
<link rel="stylesheet" href="https://fonts.googleapis.com/css2?family=Libre+Baskerville:wght@700&family=Open+Sans:wght@400;700&display=swap">
<style>
  :root {
    --bg: #a9a9a9;
    --paper: #ffffff;
    --brand-blue: #2a5db0;
    --brand-blue-dark: #1f4b96;
    --art-light: #dbe7f5;
    --art-mid: #9fc0e6;
    --fold-grey: #d6d8db;
    --insert-edge: #dfe1e4;
    --text-dark: #2b2b2b;
    --text-muted: #6b6f75;
    --photo-tone-a: #8a7a66;
    --photo-tone-b: #c9b89c;
  }
  * { margin: 0; padding: 0; box-sizing: border-box; }
  html, body { width: 1200px; height: 1072px; overflow: hidden; }
  body {
    background: var(--bg);
    font-family: "Open Sans", Arial, sans-serif;
    position: relative;
  }
  .folder-cover, .folder-inside {
    position: absolute;
    top: 296px;
    height: 480px;
    box-shadow: 0 8px 22px rgba(0,0,0,0.25);
  }
  .folder-cover { left: 40px; width: 360px; }
  .folder-inside { left: 440px; width: 720px; }
  svg { display: block; }
  .brand-name {
    font-family: "Libre Baskerville", Georgia, serif;
    font-weight: 700;
    fill: var(--brand-blue);
  }
  .insert-heading { font-family: "Open Sans", Arial, sans-serif; font-weight: 700; fill: var(--brand-blue); }
  .insert-body { font-family: "Open Sans", Arial, sans-serif; font-weight: 400; fill: var(--text-dark); }
  .insert-muted { font-family: "Open Sans", Arial, sans-serif; font-weight: 400; fill: var(--text-muted); }
</style>
</head>
<body>

<!-- Front cover -->
<div class="folder-cover">
  <svg width="360" height="480" viewBox="0 0 360 480">
    <defs>
      <linearGradient id="coverArtTone" x1="0" y1="1" x2="1" y2="0">
        <stop offset="0" stop-color="var(--paper)"/>
        <stop offset="0.55" stop-color="var(--art-light)"/>
        <stop offset="1" stop-color="var(--brand-blue)"/>
      </linearGradient>
      <linearGradient id="insertArtTone" x1="0" y1="1" x2="1" y2="0">
        <stop offset="0" stop-color="var(--paper)"/>
        <stop offset="1" stop-color="var(--art-mid)"/>
      </linearGradient>
      <linearGradient id="lumberTone" x1="0" y1="0" x2="1" y2="1">
        <stop offset="0" stop-color="var(--photo-tone-b)"/>
        <stop offset="1" stop-color="var(--photo-tone-a)"/>
      </linearGradient>
    </defs>
    <rect class="cover-paper" width="360" height="480" fill="var(--paper)"/>
    <rect class="cover-artwork" x="0" y="0" width="360" height="330" fill="url(#coverArtTone)" role="img" aria-label="Decorative blue corner and light blue swoosh artwork"/>
    <circle class="brand-mark" cx="60" cy="410" r="14" fill="var(--brand-blue)"/>
    <text class="brand-name" x="84" y="416" font-size="16">CALVERDANE GROUP</text>
  </svg>
</div>

<!-- Inside spread -->
<div class="folder-inside">
  <svg width="720" height="480" viewBox="0 0 720 480">
    <rect class="inside-paper" width="720" height="480" fill="var(--paper)"/>
    <line class="fold-line" x1="360" y1="0" x2="360" y2="480" stroke="var(--fold-grey)" stroke-width="1.5"/>

    <!-- Profile brochure insert -->
    <g class="profile-insert">
      <rect x="400" y="40" width="270" height="300" fill="var(--paper)" stroke="var(--insert-edge)"/>
      <rect class="insert-artwork" x="590" y="41" width="79" height="90" fill="url(#insertArtTone)" role="img" aria-label="Decorative blue corner artwork"/>
      <circle cx="422" cy="72" r="9" fill="var(--brand-blue)"/>
      <text class="brand-name" x="437" y="77" font-size="11">CALVERDANE GROUP</text>
      <text class="insert-heading" x="416" y="112" font-size="9">ABOUT OUR GROUP</text>
      <text class="insert-muted" x="416" y="130" font-size="7.5">Lumber and panel supply</text>
      <text class="insert-muted" x="416" y="141" font-size="7.5">for industrial buyers</text>
      <text class="insert-muted" x="416" y="152" font-size="7.5">Dubai · Canada · Logistics</text>
      <text class="insert-body" x="416" y="176" font-size="7">We source, mill and ship</text>
      <text class="insert-body" x="416" y="186" font-size="7">timber and panel products</text>
      <text class="insert-body" x="416" y="196" font-size="7">to wholesalers, manufacturers</text>
      <text class="insert-body" x="416" y="206" font-size="7">and large industries worldwide since</text>
      <text class="insert-body" x="416" y="216" font-size="7">our founding.</text>
      <rect class="insert-photo" x="550" y="170" width="106" height="150" fill="url(#lumberTone)" role="img" aria-label="Photograph of stacked lumber in a timber yard"/>
    </g>

    <!-- Pocket -->
    <path class="pocket" d="M360 320 L720 280 V480 H360 Z" fill="var(--brand-blue)"/>
    <path class="pocket-edge" d="M360 320 L720 280" fill="none" stroke="var(--brand-blue-dark)" stroke-width="2"/>
    <g class="card-slits" stroke="var(--brand-blue-dark)" stroke-width="2">
      <line x1="560" y1="390" x2="574" y2="378"/>
      <line x1="640" y1="390" x2="626" y2="378"/>
    </g>
  </svg>
</div>

</body>
</html>
```